Aldercrest Chiropractic Rehabilitation and Wellness
Business Card, Portfolio Folder, Stationary, Postcard
Simple
Marlow Tenney
Doctor of Chiropractic
518 Verbena Ridge Avenue
Chico, CA 95926
marlow@alderbrook.com
www.alderbrook.com
Fonts are TrajanPro and Corbel
Logo and URL or just logo
Logo
jpg Logo

```html
<!DOCTYPE html>
<html lang="en">
<head>
<meta charset="utf-8">
<title>Aldercrest Chiropractic Rehabilitation and Wellness — Stationery</title>
<link href="https://fonts.googleapis.com/css2?family=Cinzel:wght@600&family=Source+Sans+3:wght@400;600&display=swap" rel="stylesheet">
<style>
:root{
  --blue:#1f5fa8;
  --blue-deep:#14427a;
  --green:#7cb342;
  --green-deep:#4f8a24;
  --ink:#222;
  --grey:#8a8a8a;
  --line:#d4d4d4;
  --paper:#fff;
  --stage:#fff;
  --cell:#e6e6e6;
}
*{box-sizing:border-box;margin:0;padding:0}
html,body{width:1200px;height:451px;overflow:hidden;background:var(--stage)}
body{position:relative;font-family:"Source Sans 3",sans-serif;color:var(--ink)}
.sheet{position:absolute;background:var(--paper);box-shadow:0 1px 4px rgba(0,0,0,.28);overflow:hidden}
.bar{position:absolute;left:0;height:14px}
.bar--blue{background:linear-gradient(90deg,var(--blue-deep),var(--blue) 60%,rgba(31,95,168,0))}
.bar--green{background:linear-gradient(90deg,var(--green-deep),var(--green) 60%,rgba(124,179,66,0))}
.brand{position:absolute;display:flex;align-items:center;gap:4px}
.brand__dot{border-radius:50%;background:var(--blue);flex:none}
.brand__name{font-family:"Cinzel",serif;font-weight:600;color:var(--blue);line-height:1;white-space:nowrap}
.brand--dark .brand__dot{background:#111}
.brand--dark .brand__name{color:#111}
.tagline{position:absolute;font-size:5px;color:var(--grey);white-space:nowrap}
.tagline::before{content:"";display:inline-block;width:4px;height:4px;background:var(--blue);margin-right:3px;vertical-align:middle}
.url{position:absolute;font-size:5px;color:var(--blue);white-space:nowrap}
/* fax */
.fax__title{position:absolute;right:14px;top:80px;font-weight:600;font-size:9px}
.fax__table{position:absolute;left:14px;right:14px;top:92px;border-collapse:collapse;font-size:5px}
.fax__table td{border:1px solid var(--line);height:12px;padding:0 3px}
.fax__table .lbl{background:var(--cell);width:32px;color:#555}
.fax__checks{position:absolute;left:14px;right:14px;top:150px;display:flex;justify-content:space-between;font-size:4.5px;color:#555}
.fax__checks span::before{content:"";display:inline-block;width:4px;height:4px;border:1px solid #777;margin-right:2px;vertical-align:middle}
/* cards */
.card{width:94px;height:60px}
.card__info{position:absolute;left:8px;top:30px;font-size:3.6px;line-height:4.6px;color:#555}
.card__info b{color:var(--ink);font-weight:600}
/* envelopes */
.env__flap{position:absolute;inset:0}
</style>
</head>
<body>

<!-- notecards -->
<section class="sheet notecard" style="left:29px;top:112px;width:273px;height:140px">
  <div class="bar bar--blue" style="top:26px;width:95px"></div>
  <div class="brand" style="left:96px;top:24px"><span class="brand__dot" style="width:16px;height:16px"></span><span class="brand__name" style="font-size:13px">Aldercrest</span></div>
  <p class="tagline" style="left:26px;top:46px">518 Verbena Ridge Avenue, Chico, CA</p>
  <p class="url" style="right:14px;bottom:12px">www.alderbrook.com</p>
</section>

<section class="sheet notecard" style="left:96px;top:220px;width:293px;height:135px">
  <div class="bar bar--green" style="top:20px;width:100px"></div>
  <div class="brand" style="left:100px;top:17px"><span class="brand__dot" style="width:16px;height:16px"></span><span class="brand__name" style="font-size:13px">Aldercrest</span></div>
  <p class="tagline" style="left:28px;top:40px">518 Verbena Ridge Avenue, Chico, CA</p>
  <p class="url" style="right:14px;bottom:12px">www.alderbrook.com</p>
</section>

<!-- letterhead -->
<section class="sheet letterhead" style="left:305px;top:43px;width:260px;height:305px">
  <div class="bar bar--blue" style="top:10px;width:100px"></div>
  <div class="brand" style="left:102px;top:6px"><span class="brand__dot" style="width:18px;height:18px"></span><span class="brand__name" style="font-size:14px">Aldercrest</span></div>
  <p class="tagline" style="left:24px;top:30px">518 Verbena Ridge Avenue, Chico, CA 95926</p>
  <p class="url" style="right:14px;bottom:10px">www.alderbrook.com</p>
</section>

<!-- fax cover -->
<section class="sheet fax" style="left:588px;top:43px;width:258px;height:305px">
  <div class="bar bar--blue" style="top:10px;width:98px"></div>
  <div class="brand" style="left:100px;top:6px"><span class="brand__dot" style="width:18px;height:18px"></span><span class="brand__name" style="font-size:14px">Aldercrest</span></div>
  <p class="fax__title">FAX</p>
  <table class="fax__table">
    <tr><td class="lbl">To:</td><td></td><td class="lbl">From:</td><td></td></tr>
    <tr><td class="lbl">Fax:</td><td></td><td class="lbl">Pages:</td><td></td></tr>
    <tr><td class="lbl">Phone:</td><td></td><td class="lbl">Date:</td><td></td></tr>
    <tr><td class="lbl">Re:</td><td></td><td class="lbl">CC:</td><td></td></tr>
  </table>
  <div class="fax__checks"><span>Urgent</span><span>For review</span><span>Please comment</span><span>Please reply</span><span>Please recycle</span></div>
  <p class="url" style="right:14px;bottom:10px">www.alderbrook.com</p>
</section>

<!-- business cards -->
<section class="sheet card" style="left:878px;top:43px">
  <div class="bar bar--blue" style="top:8px;width:34px;height:8px"></div>
  <div class="brand" style="left:36px;top:6px"><span class="brand__dot" style="width:9px;height:9px"></span><span class="brand__name" style="font-size:7px">Aldercrest</span></div>
  <p class="card__info"><b>Marlow Tenney</b><br>Doctor of Chiropractic<br>518 Verbena Ridge Avenue<br>marlow@alderbrook.com</p>
</section>
<section class="sheet card" style="left:982px;top:43px">
  <div class="bar bar--green" style="top:8px;width:34px;height:8px"></div>
  <div class="brand" style="left:36px;top:6px"><span class="brand__dot" style="width:9px;height:9px"></span><span class="brand__name" style="font-size:7px">Aldercrest</span></div>
  <p class="card__info"><b>Marlow Tenney</b><br>Doctor of Chiropractic<br>518 Verbena Ridge Avenue<br>marlow@alderbrook.com</p>
</section>
<section class="sheet card" style="left:878px;top:119px">
  <div class="brand brand--dark" style="left:18px;top:20px"><span class="brand__dot" style="width:16px;height:16px"></span><span class="brand__name" style="font-size:8px">Aldercrest</span></div>
</section>
<section class="sheet card" style="left:982px;top:119px">
  <div class="brand" style="left:18px;top:20px"><span class="brand__dot" style="width:16px;height:16px"></span><span class="brand__name" style="font-size:8px">Aldercrest</span></div>
</section>

<!-- envelope back -->
<section class="sheet envelope" style="left:840px;top:205px;width:290px;height:120px">
  <svg class="env__flap" viewBox="0 0 290 120" preserveAspectRatio="none"><path d="M0 0 L145 62 L290 0" fill="none" stroke="var(--line)" stroke-width="1"/></svg>
  <span class="brand__dot" style="position:absolute;left:135px;top:50px;width:20px;height:20px;border-radius:50%;background:var(--blue)"></span>
</section>

<!-- envelope front -->
<section class="sheet envelope" style="left:876px;top:256px;width:288px;height:100px">
  <svg class="env__flap" viewBox="0 0 288 100" preserveAspectRatio="none"><path d="M0 0 L144 50 L288 0 Z" fill="#eeeeee" stroke="var(--line)" stroke-width="1"/></svg>
  <span style="position:absolute;left:132px;top:38px;width:24px;height:24px;border-radius:50%;background:#111"></span>
</section>

</body>
</html>
```